Bref créative
VerdaLune
Business Cards etc...
Professional
Carmen Delvoe
Owner
3284-B Willow Crest Rd. #261
Greensboro, NC 27490
verdalunenc@mailbox.example
www.VerdaLuneNC.example
Landscape Management Services
Striving for earth friendly services
Member of 2% Pour Le Sol, Has a logo
landscaping | hardscapes | lighting | irrigation | water features | design | walls | patios | contract lawncare |

```html
<!DOCTYPE html>
<html lang="en">
<head>
<meta charset="utf-8">
<title>VerdaLune Business Card</title>
<link href="https://fonts.googleapis.com/css2?family=Source+Sans+3:wght@400;600;700;800&display=swap" rel="stylesheet">
<style>
  :root {
    --backdrop: #ece6dd;
    --card: #ffffff;
    --green: #3b7a38;
    --green-dark: #2f6a2f;
    --green-light: #8cbf5f;
    --ink: #2b2b2b;
    --rule: #8cbf5f;
  }
  * { box-sizing: border-box; margin: 0; padding: 0; }
  html, body { width: 1200px; height: 965px; overflow: hidden; }
  body {
    background: var(--backdrop);
    font-family: "Source Sans 3", "Myriad Pro", sans-serif;
    position: relative;
  }
  .card {
    position: absolute;
    left: 120px; top: 209px;
    width: 960px; height: 547px;
    background: var(--card);
    border-radius: 30px;
    overflow: hidden;
    box-shadow: 0 6px 18px rgba(0,0,0,0.18);
  }
  .card-wave { position: absolute; left: 0; top: 0; width: 960px; height: 547px; }
  .brand {
    position: absolute; left: 81px; top: 62px;
    display: flex; align-items: center; gap: 30px;
  }
  .brand-mark {
    width: 140px; height: 140px; border-radius: 50%;
    background: var(--green);
    flex: none;
  }
  .brand-name {
    font-size: 128px; font-weight: 800; color: var(--green);
    line-height: 1; letter-spacing: -1px;
  }
  .tagline {
    position: absolute; left: 257px; top: 198px;
    font-size: 21px; font-weight: 700; color: var(--green);
    letter-spacing: 5px; text-transform: uppercase;
    white-space: nowrap;
  }
  .person { position: absolute; left: 163px; top: 340px; }
  .person-name { font-size: 31px; font-weight: 600; color: var(--green); line-height: 1.1; }
  .person-role { font-size: 21px; font-weight: 600; color: var(--ink); line-height: 1.2; }
  .divider {
    position: absolute; left: 452px; top: 286px;
    width: 2px; height: 196px; background: var(--rule);
  }
  .contact { position: absolute; left: 478px; top: 282px; list-style: none; }
  .contact li {
    font-size: 25px; color: var(--ink); height: 39px; line-height: 39px;
    display: flex; align-items: center; white-space: nowrap;
  }
  .contact .plain { padding-left: 32px; }
  .contact .icon { width: 22px; height: 22px; margin-right: 10px; flex: none; }
</style>
</head>
<body>
  <div class="card">
    <svg class="card-wave" viewBox="0 0 960 547" aria-hidden="true">
      <path d="M0,405 C250,470 600,510 960,505 L960,547 L0,547 Z" fill="var(--green-light)"/>
      <path d="M0,438 C260,500 620,525 960,520 L960,547 L0,547 Z" fill="var(--green-dark)"/>
    </svg>

    <div class="brand">
      <div class="brand-mark"></div>
      <div class="brand-name">VerdaLune</div>
    </div>
    <div class="tagline">Grow &amp; Nurture Your Outdoor Space</div>

    <div class="person">
      <div class="person-name">Carmen Delvoe</div>
      <div class="person-role">Owner</div>
    </div>

    <div class="divider"></div>

    <ul class="contact">
      <li class="plain">3284-B Willow Crest Rd. #261</li>
      <li class="plain">Greensboro, NC 27490</li>
      <li>
        <svg class="icon" viewBox="0 0 24 24"><path d="M6 2 C3 3 2 6 4 10 C7 16 11 20 16 22 C19 23 21 21 22 19 L18 15 L15 17 C12 15 9 12 7 9 L9 6 Z" fill="var(--green)"/></svg>
        <span>336-555-0148</span>
      </li>
      <li>
        <svg class="icon" viewBox="0 0 24 24"><text x="12" y="19" text-anchor="middle" font-size="22" font-weight="700" fill="var(--ink)" font-family="Source Sans 3, sans-serif">@</text></svg>
        <span>verdalunenc@mailbox.example</span>
      </li>
      <li>
        <svg class="icon" viewBox="0 0 24 24" fill="none" stroke="var(--green)" stroke-width="2"><circle cx="12" cy="12" r="10"/><ellipse cx="12" cy="12" rx="4.5" ry="10"/><line x1="2" y1="12" x2="22" y2="12"/></svg>
        <span>www.VerdaLuneNC.example</span>
      </li>
    </ul>
  </div>
</body>
</html>
```